Accountability Project Graphics

I want to create 10 social media graphics (new Instagram size 4:5 (1080 x 1350 pixels) focusing on our Kelmora Accountability App, using any of the 3 pictures attached. Use the attached pics only, NO RANDOM STOCK PHOTOGRAPHY. For the color scheme, use the landing page colors/fonts (attached).
You can add any of the 3 photos attached but I mainly need BOLD text that includes these headlines and sub-headlines on them.
Please NOTE for all the headlines below, also add this sub-headline on each graphic:
Stay Consistent with MB in Your Pocket!
Here are the headlines:
• Stop Starting Over Every Monday
• You don't need more willpower. You need more support
• Built for women who are tired of doing this alone
• When Motivation Fades, MB Checks In
• The Support System You've Been Missing
• Support When Motivation Disappears
• What if MB Checked in Every Day?
• The Missing Piece Isn't Another Diet
• Eat the food you love. Stay accountable every day.
• One Bad Meal Doesn't Mean You Failed
women over 40 trying to lose weight

```html
<!DOCTYPE html>
<html lang="en">
<head>
<meta charset="utf-8">
<title>Kelmora Accountability App – Social Graphics</title>
<link rel="stylesheet" href="https://fonts.googleapis.com/css2?family=Playfair+Display:ital,wght@0,700;0,900;1,700;1,900&family=Mukta:wght@600;700&family=Yellowtail&display=swap">
<style>
  :root {
    --pink: #e0215f;
    --pink-soft: #f6d3dd;
    --blush: #fbe8ee;
    --blush-deep: #f4d6df;
    --ink: #111111;
    --white: #ffffff;
    --steel: #9a9a9a;
  }
  * { box-sizing: border-box; margin: 0; padding: 0; }
  html, body { width: 1200px; height: 1000px; overflow: hidden; background: var(--white); }
  .board { position: relative; width: 1200px; height: 1000px; background: var(--white); }

  .post { position: absolute; overflow: hidden; background: var(--blush); }
  .post--stop      { left: 91px;  top: 106px; width: 302px; height: 377px; }
  .post--support   { left: 450px; top: 106px; width: 301px; height: 377px; }
  .post--alone     { left: 809px; top: 103px; width: 303px; height: 380px; background: linear-gradient(180deg, #fbe6ec, #f6e3ea); }
  .post--checks    { left: 278px; top: 534px; width: 303px; height: 379px; }
  .post--missing   { left: 636px; top: 534px; width: 303px; height: 379px; }

  .abs { position: absolute; }
  .serif { font-family: "Playfair Display", "Times New Roman", serif; font-weight: 900; color: var(--ink); line-height: 1; }
  .script { font-family: "Yellowtail", cursive; color: var(--ink); line-height: 1; }

  .soft-disc { position: absolute; border-radius: 50%; background: var(--blush-deep); opacity: .55; }

  .photo { position: absolute; }

  .tag {
    position: absolute; background: var(--pink); color: var(--white);
    font-family: "Playfair Display", serif; font-weight: 700; text-align: center; line-height: 1;
    display: flex; align-items: center; justify-content: center; letter-spacing: .02em; white-space: nowrap;
  }
  .tag i { font-style: italic; font-weight: 700; }

  .stamp {
    position: absolute; border: 3px solid var(--pink); border-radius: 6px; background: var(--white);
    color: var(--pink); font-family: "Playfair Display", serif; font-weight: 900;
    display: flex; align-items: center; justify-content: center; line-height: 1;
  }

  .cta { position: absolute; background: var(--pink); color: var(--white); font-family: "Mukta", sans-serif; font-weight: 700; line-height: 1.15; }
  .cta em { font-style: italic; }
  .cta--edge { border-top: 3px solid #c9c9c9; }

  .stop-photo { left: 146px; top: 28px; width: 156px; height: 349px; border-radius: 80px 80px 0 0;
    background: linear-gradient(160deg, #f3c9d5 0%, #4a3a3c 35%, #1b1719 70%, #2a2426 100%); }
  .stop-floor { left: 0; top: 326px; width: 302px; height: 51px; background: linear-gradient(180deg, #5a5a5a, #2d2d2d); }
  .stop-line { left: 26px; top: 264px; }

  .rule { position: absolute; height: 1px; background: #555; top: 41px; }
  .app-name { font-family: "Playfair Display", "Times New Roman", serif; font-weight: 700; color: var(--ink); line-height: 1; }
</style>
</head>
<body>
<main class="board">

  <section class="post post--stop">
    <div class="soft-disc" style="left:180px; top:-90px; width:200px; height:200px;"></div>
    <div class="photo stop-floor" aria-hidden="true"></div>
    <div class="photo stop-photo" role="img" aria-label="Photo of the coach in a black lace top, smiling with hand on hip"></div>
    <div class="stamp" style="left:11px; top:34px; width:128px; height:62px; font-size:36px;">STOP</div>
    <div class="abs serif" style="left:10px; top:110px; font-size:31px;">Starting</div>
    <div class="abs serif" style="left:9px; top:146px; font-size:40px;">OVER</div>
    <div class="abs serif" style="left:10px; top:188px; font-size:33px; color:var(--pink);">EVERY</div>
    <div class="abs serif" style="left:11px; top:224px; font-size:31px; color:var(--pink);">Monday</div>
    <svg class="abs stop-line" width="100" height="8" viewBox="0 0 100 8" aria-hidden="true">
      <path d="M2 6 Q50 0 98 5" stroke="#e0215f" stroke-width="2.5" fill="none" stroke-linecap="round"/>
    </svg>
    <div class="cta" style="left:0; top:284px; width:158px; height:44px; padding:5px 0 0 14px; font-size:12px;">
      Stay Consistent with<br><em style="font-size:14px;">MB in Your Pocket!</em>
    </div>
  </section>

  <section class="post post--support">
    <div class="soft-disc" style="left:175px; top:-80px; width:220px; height:220px;"></div>
    <div class="soft-disc" style="left:-70px; top:285px; width:180px; height:180px;"></div>
    <div class="tag" style="left:55px; top:28px; width:191px; height:19px; font-size:15px;">YOU&nbsp;<i>DON'T</i>&nbsp;NEED</div>
    <div class="abs serif" style="left:0; width:301px; text-align:center; top:50px; font-size:58px;">MORE</div>
    <div class="abs serif" style="left:0; width:301px; text-align:center; top:110px; font-size:42px;">WILLPOWER</div>
    <div class="tag" style="left:93px; top:158px; width:113px; height:18px; font-size:15px;">YOU&nbsp;<i>NEED</i></div>
    <div class="abs serif" style="left:0; width:301px; text-align:center; top:179px; font-size:58px;">MORE</div>
    <div class="abs serif" style="left:0; width:301px; text-align:center; top:238px; font-size:47px;">SUPPORT</div>
    <div class="cta" style="left:54px; top:300px; width:192px; height:54px; padding:7px 0 0 16px; font-size:14px; border:2px solid #b9b9b9; border-radius:3px;">
      Stay Consistent with<br><em style="font-size:17px;">MB in Your Pocket!</em>
    </div>
  </section>

  <section class="post post--alone">
    <div class="photo" role="img" aria-label="Photo of the coach laughing and hugging a friend in a store"
         style="left:150px; top:0; width:153px; height:298px; background: linear-gradient(90deg, rgba(246,227,234,0) 0%, #e3779c 30%, #d9b4a6 60%, #b7c7a9 100%);"></div>
    <div class="abs script" style="left:38px; top:30px; font-size:64px;">Built</div>
    <div class="tag" style="left:80px; top:100px; width:33px; height:13px; font-size:9px;">FOR</div>
    <div class="abs serif" style="left:24px; top:116px; font-size:30px;">WOMEN</div>
    <div class="tag" style="left:70px; top:152px; width:57px; height:14px; font-size:9px;">WHO ARE</div>
    <div class="abs script" style="left:36px; top:166px; font-size:60px;">tired</div>
    <div class="tag" style="left:46px; top:230px; width:85px; height:14px; font-size:9px;">OF DOING THIS</div>
    <div class="abs serif" style="left:9px; top:248px; font-size:44px;">ALONE</div>
    <div class="cta cta--edge" style="left:0; top:302px; width:303px; height:78px; padding:7px 0 0 15px; font-size:24px;">
      Stay Consistent with<br><em style="font-size:28px;">MB in Your Pocket!</em>
    </div>
  </section>

  <section class="post post--checks">
    <div class="soft-disc" style="left:215px; top:-40px; width:150px; height:160px;"></div>
    <div class="soft-disc" style="left:-60px; top:300px; width:120px; height:120px;"></div>
    <div class="rule" style="left:53px; width:48px;"></div>
    <div class="rule" style="left:204px; width:63px;"></div>
    <div class="abs serif" style="left:0; width:303px; text-align:center; top:20px; font-size:38px; font-weight:700; color:var(--pink);">When</div>
    <div class="abs serif" style="left:0; width:303px; text-align:center; top:58px; font-size:33px; font-weight:700;">Motivation Fades,</div>
    <div class="abs app-name" style="left:0; width:303px; text-align:center; top:160px; font-size:80px;">MB</div>
    <div class="abs serif" style="left:0; width:303px; text-align:center; top:290px; font-size:37px; font-weight:700;">Checks In</div>
    <div class="cta cta--edge" style="left:0; top:340px; width:303px; height:39px; padding:9px 0 0 12px; font-size:14px;">
      Stay Consistent with&nbsp; <em>MB in Your Pocket!</em>
    </div>
  </section>

  <section class="post post--missing">
    <div class="abs serif" style="left:0; width:303px; text-align:center; top:8px; font-size:25px; font-weight:700;">THE</div>
    <div class="tag" style="left:0; top:37px; width:300px; height:37px; font-size:29px; font-weight:700; letter-spacing:0;">SUPPORT SYSTEM</div>
    <div class="abs serif" style="left:12px; top:90px; font-size:27px; font-weight:700;">You've Been</div>
    <div class="stamp" style="left:176px; top:88px; width:120px; height:40px; font-size:21px;">MISSING</div>
    <div class="photo" role="img" aria-label="Photo of the coach laughing and hugging a woman with curly hair"
         style="left:0; top:134px; width:303px; height:206px; background: linear-gradient(120deg, #f0dde6 0%, #e07b9d 35%, #3b3150 55%, #d9e6b6 80%, #ecdde8 100%);"></div>
    <div class="cta cta--edge" style="left:0; top:340px; width:303px; height:39px; padding:9px 0 0 12px; font-size:14px;">
      Stay Consistent with&nbsp; <em>MB in Your Pocket!</em>
    </div>
  </section>

</main>
</body>
</html>
```